Medical "Travel" Folder for our Clients - One Side (Back and Cover)

We are seeking a cover (binder) that represents the image of our clinic and our country.

We operate primarily in the field of Occupational Health, with a strong expertise in the Maritime sector.

This cover/folder is a product that will serve as a document cover folder for safekeeping of medical documents and other documents, which our customers have to carry around the world.

* Please refer to the attachment File 2 for presentation folder specifications.

We are looking for elements related to Portugal - Lisbon and Sintra and elements related to the Maritime industry (mainly cruise ships, tankers and Oil Platforms). Samples Photos provided. Feel free to use other royal free photos.

We enclose our logo and some pictures to use (can use other material).

Would be great if you choose other photos or elements from photos, from this ones. Take in consideration Royal Free Photos.

Furthermore in order to facilitate graphic work we’re attaching a graphical guide that we will use to print the cover. We ask you to follow the instructions given by the commercial printers, please.

Information to be contemplated on the cover:
Tavrelo – Núcleo Integrado do Bem-Estar, Lda
Rua Joaquim Barradas Pinto Numero 9, 3ºE
2860-392 Queluz, Portugal
E-mail: geral@tavrelo.pt
www: http://www.tavrelo.pt
Telefone/Phone/Fax: +351 21 8062917
Telemóvel/Mobile: +351 963150486

Project Deadline Extended Reason: Dear PixelHarbor,As a second experience we are not happy with the result... only 3 days left and had one design submited ... Already upgraded the the value and we think is a very fair value.We would like to extend 10 days if possible. Added Tuesday, June 23, 2015

Hello Designers,Please use the template provided in the files in order for us to evaluate the designs, otherwise we will not accept it due to the printing company guidelines (also provided in the attached files) Added Friday, June 26, 2015

Thank you for all designs submitted. We will review them today.Please present all the designs with the appropriate template instead of only one page. Added Monday, June 29, 2015

Dear designers,May our description didn't provide a clear detail back and cover. We are going to print one side, with back and cover, and not 2 sides. This means that you call fill the template AREA. Added Tuesday, June 30, 2015

Project Deadline Extended Reason: Due to the confusion with the title. We want one SIDE (with back and cover) Added Tuesday, June 30, 2015

Just upgraded our Budget to get more Designs.Also upgraded the deadline.This deadline will be the final one. Added Tuesday, June 30, 2015

Industry/Entity Type

Healthcare

Colors
f37122
3176b5
85abd2

Requirements
Must have
• Only one side (use all the template area) is used/visible with the four or two colors. ( We would like to use the colors that we have in our logo, but we will accept different color shades.
• Photos - (uploaded new 2 photos)
Nice to have
• Icons can be used to identify emails, web pages, phone, etc.
• Designer can use other fonts. The ones attached refers to the logo.
• Added a few templates that we use with colourful elements that would be interesting using.
• Minimal Design.
• Portuguese Flag :)
• Can transform or convert the photos as much as you want (like using filters for instance).
• Medical Elements.
• We would like you to get as much creativity as you can be.
Should not have
• Templates different from the one provided.
• Our logo changed. However we can allow turning the logo into one or two colors (something we can use in the future as a logo redesign)

```html
<!DOCTYPE html>
<html lang="pt">
<head>
<meta charset="utf-8">
<title>Tavrelo – Presentation Folder, Outside</title>
<link rel="stylesheet" href="https://fonts.googleapis.com/css2?family=Arimo:wght@400;700&display=swap">
<style>
  :root {
    --paper: #ffffff;
    --navy: #0e2c8c;
    --navy-deep: #0a2170;
    --royal: #1f57c8;
    --sky: #3a8ee6;
    --cyan: #5fe6ef;
    --stripe-cyan: #6fd3f2;
    --orange: #f0561a;
    --spine: #2f72d6;
    --trim: #9cc6ea;
    --ink: #1b2f8f;
    --dim: #777777;
    --legend-orange: #f26a2e;
  }
  html, body {
    margin: 0;
    padding: 0;
    background: var(--paper);
    overflow: hidden;
  }
  .canvas {
    width: 1200px;
    height: 926px;
    display: block;
    font-family: "Arimo", Arial, sans-serif;
  }
  .dimension-label { fill: var(--dim); font-size: 9px; }
  .dimension-line { stroke: var(--dim); stroke-width: 0.7; }
  .trim-line { fill: none; stroke: var(--trim); stroke-width: 1; }
  .brand-name { fill: var(--ink); font-weight: 700; font-size: 25px; letter-spacing: 0.3px; }
  .brand-tagline { fill: var(--ink); font-weight: 700; font-size: 5.8px; }
  .contact-line { fill: var(--ink); font-weight: 700; font-size: 8.4px; }
  .emboss-name { fill: var(--navy); font-weight: 700; font-size: 13px; }
  .legend-title { fill: var(--legend-orange); font-size: 12px; }
  .legend-label { fill: #222; font-size: 8.5px; }
  .legend-box { fill: none; stroke: #888; stroke-width: 0.8; }
</style>
</head>
<body>
<svg class="canvas" viewBox="0 0 1165 900" preserveAspectRatio="none" xmlns="http://www.w3.org/2000/svg">
  <defs>
    <linearGradient id="flap-left-fill" x1="0" y1="0" x2="1" y2="1">
      <stop offset="0" stop-color="#12368f"/>
      <stop offset="1" stop-color="#1a3f9c"/>
    </linearGradient>
    <linearGradient id="back-panel-fill" x1="0" y1="0" x2="1" y2="1">
      <stop offset="0" stop-color="#0c2a8e"/>
      <stop offset="0.55" stop-color="#1647b5"/>
      <stop offset="1" stop-color="#2f7ae0"/>
    </linearGradient>
    <radialGradient id="front-panel-fill" cx="1" cy="0.85" r="1.1">
      <stop offset="0" stop-color="#5ef0f2"/>
      <stop offset="0.45" stop-color="#3aa3ea"/>
      <stop offset="1" stop-color="#1d55c9"/>
    </radialGradient>
    <linearGradient id="pocket-fill" x1="0" y1="0" x2="1" y2="0.6">
      <stop offset="0" stop-color="#0f2f98"/>
      <stop offset="1" stop-color="#2f82e0"/>
    </linearGradient>
    <linearGradient id="flag-fill" x1="0" y1="0" x2="1" y2="0">
      <stop offset="0.1" stop-color="#2a9a35"/>
      <stop offset="0.3" stop-color="#d8301e"/>
      <stop offset="1" stop-color="#e8201c"/>
    </linearGradient>
    <clipPath id="photo-band">
      <polygon points="958,58 1102,58 470,697 318,697"/>
    </clipPath>
  </defs>

  <g class="dimensions">
    <line class="dimension-line" x1="55" y1="18" x2="1147" y2="18"/>
    <line class="dimension-line" x1="55" y1="12" x2="55" y2="50"/>
    <line class="dimension-line" x1="1147" y1="12" x2="1147" y2="50"/>
    <text class="dimension-label" x="585" y="15" text-anchor="middle">530 mm</text>
    <line class="dimension-line" x1="16" y1="58" x2="16" y2="882"/>
    <line class="dimension-line" x1="10" y1="58" x2="48" y2="58"/>
    <line class="dimension-line" x1="10" y1="882" x2="250" y2="882"/>
    <text class="dimension-label" x="13" y="378" text-anchor="middle" transform="rotate(-90 13 378)">400 mm</text>
  </g>

  <polygon class="trim-line" points="46,72 218,52 1152,52 1152,702 688,702 670,887 254,887 236,702 218,702 46,684"/>

  <polygon class="side-flap" fill="url(#flap-left-fill)" points="50,75 218,58 218,697 50,680"/>

  <rect class="spine" x="218" y="58" width="22" height="639" fill="var(--spine)"/>
  <line x1="229" y1="58" x2="229" y2="697" stroke="#5a96e6" stroke-width="0.8"/>

  <rect class="back-panel" x="240" y="58" width="443" height="639" fill="url(#back-panel-fill)"/>
  <polygon fill="var(--orange)" points="240,58 465,58 240,290"/>
  <polygon fill="var(--stripe-cyan)" points="466,58 478,58 240,302 240,290"/>
  <text class="emboss-name" x="308" y="130" text-anchor="middle">TAVRELO</text>

  <rect class="front-panel" x="705" y="58" width="442" height="639" fill="url(#front-panel-fill)"/>

  <rect class="spine" x="683" y="58" width="22" height="639" fill="var(--spine)"/>
  <line x1="694" y1="58" x2="694" y2="697" stroke="#5a96e6" stroke-width="0.8"/>

  <polygon fill="var(--navy-deep)" points="935,58 952,58 315,697 298,697"/>
  <polygon fill="#3c7fdc" points="952,58 958,58 318,697 312,697"/>
  <polygon fill="var(--navy)" points="1102,58 1118,58 488,697 470,697" opacity="0.9"/>
  <polygon fill="var(--stripe-cyan)" points="1090,58 1102,58 470,697 458,697"/>

  <g class="photo-band" clip-path="url(#photo-band)">
    <rect x="300" y="58" width="820" height="639" fill="#8fd0f0"/>
    <rect role="img" aria-label="Photo: doctor's hands taking a patient's pulse" x="300" y="58" width="820" height="62" fill="#c9dbe8"/>
    <rect role="img" aria-label="Photo: stethoscope close-up in blue tones" x="300" y="125" width="820" height="140" fill="#3a5fd8"/>
    <rect role="img" aria-label="Photo: clinician at a medical workstation" x="300" y="269" width="820" height="66" fill="#b8c6d4"/>
    <rect role="img" aria-label="Photo: clear sky over the harbour" x="300" y="340" width="820" height="66" fill="#7fb8ea"/>
    <rect role="img" aria-label="Photo: cruise ships moored at Lisbon harbour" x="300" y="410" width="820" height="70" fill="#6aa0c8"/>
    <rect role="img" aria-label="Photo: suspension bridge over the Tagus river" x="300" y="485" width="820" height="66" fill="#7a7f82"/>
    <rect role="img" aria-label="Image: Portuguese flag" x="400" y="556" width="200" height="67" fill="url(#flag-fill)"/>
    <rect role="img" aria-label="Photo: white cruise ship at sea" x="300" y="628" width="820" height="69" fill="#9fb6cc"/>
  </g>

  <rect class="pocket-fold" x="240" y="697" width="443" height="21" fill="var(--spine)"/>
  <line x1="240" y1="707" x2="683" y2="707" stroke="#0f2f7a" stroke-width="0.8"/>
  <polygon class="pocket" fill="url(#pocket-fill)" points="240,718 683,718 665,882 258,882"/>

  <g class="brand-block">
    <circle cx="950" cy="544" r="27" fill="var(--orange)"/>
    <text class="brand-name" x="982" y="554">TAVRELO</text>
    <text class="brand-tagline" x="983" y="563">NÚCLEO INTEGRADO DO BEM-ESTAR, LDA</text>
  </g>

  <g class="contact-block">
    <text class="contact-line" x="927" y="589">Tavrelo – Núcleo Integrado do Bem-Estar, Lda</text>
    <text class="contact-line" x="927" y="600">Rua Joaquim Barradas Pinto Numero 9, 3ºE</text>
    <text class="contact-line" x="927" y="611">2860-392 Queluz, Portugal</text>
    <text class="contact-line" x="927" y="622">E-mail: geral@tavrelo.pt</text>
    <text class="contact-line" x="927" y="633">www: http://www.tavrelo.pt</text>
    <text class="contact-line" x="927" y="644">Telefone/Phone/Fax: +351 21 8062917</text>
    <text class="contact-line" x="927" y="655">Telemóvel/Mobile: +351 963150486</text>
  </g>

  <g class="legend">
    <text class="legend-title" x="957" y="779">OUTSIDE</text>
    <rect class="legend-box" x="941" y="792" width="206" height="86" rx="8"/>
    <line x1="957" y1="806" x2="988" y2="806" stroke="#111" stroke-width="1"/>
    <text class="legend-label" x="998" y="809">Size (open)</text>
    <line x1="957" y1="824" x2="988" y2="824" stroke="var(--trim)" stroke-width="1"/>
    <text class="legend-label" x="998" y="827">Margin for trimming 2 mm</text>
    <line x1="957" y1="842" x2="988" y2="842" stroke="var(--legend-orange)" stroke-width="1" stroke-dasharray="3 2"/>
    <text class="legend-label" x="998" y="845">Business card slot / Flap slot</text>
  </g>
</svg>
</body>
</html>
```